Create a responsive clean and mean platform

We support global forensic investigations (like trellmark or corvath files). We help the clients (Chief Legal Officer) to get insights on potential risks to their company and how to act on them. When in need they will immediately call us. we want to create a platform that supports the client in everydaty tasks considering forensic and risks.

Homepage (after login client): This page has following areas:
There should be a standard layout on every page with search, messages, navigation and login name (you see the client is logged in)

1. first area shows different risk and issues related to the company using the platform. There are different types of alerts and issues, like, compliance issues, risk issues, risk alerts, industry alerts and business alerts. You are able to click on the alerts and go into more details. The area of issues gives the option for view between list details or an icon view.
Second area on this page: It's big and show a map in the style provided (see screenshots). The map show an overview of new articles from around the world. The news article related to the client business are plotted on the map. Every time there is a new news feed, you will have a small pop up that shows the feed for 2 seconds top right corner. The map is interactive and also has a timeline in the bottom to slide from a year ago to now.
Third area: Shows a process status of a silver kite project. It shows the complete process and the current status.
Fourth area: Shows two overviews of budget Vs. Costs and Planned Vs. Actual. When clicking on them the client goes to a page with more detail.

Search page: We would like a search page that shows the search results of for example Corvath files. It contains two different areas. First showing are issues and risk from within the company that are related to "Corvath files". With a short description on the issue and that the issue was resolved a week ago. '
Second area: contains news related articles, with header, small picture related to "corvath files".

Issue Detail Page: Contains details about the issues and alerts you clicked from the homepage. The details contains to call to action parts: one is to navigate to get in contact for this particular issue. The second part is related document. Apart from that you also see other related issues and alerts.

Get in contact for certain issue/alert page:
Contains contact cards as shown in the style examples. On the left you first see contact card with the title Head Quarter. Contact: Maudie Ferlow with a picture of the contact. Like in the screenshot, except you can push a call button or email button.
Below another contact card in the same style with Regional. Contact: Cedric Hollaway and also you can push a call button or email button.
On the right side you see current subscription that says three things: Prevent, Detect and Repond full platinum subscription
Below just like in the example you see three experts with name photo and expertise.

Any other colors then what we included. Icons and stuff and cool graphics are always welcome.
Please use the screenshots provided as reference for the design style.

Target Market(s)

Client Chief Officer (CLO)

Industry/Entity Type

Security

Number of Pages Required

4 page

Font styles to use
Other font styles liked:
• If possible frutiger or open sans if not Sans serif

Colors
9bcb3c
0555a3
0592cd

Requirements
Must have
• It should be a clean and sterile platform. Which is light from color and uses color to accentuate risk issue's and call to action.
• Please use the following color codes: Dark blue R0 G39 B118, Green R129 G188 B0, blue R0 G161 B222, Light blue R114 G199 B231, Dark green R60 G138 B46, light green R189 G210 B3.
Nice to have
• next to desktop also one page on zuvo
Should not have
• It's a side from business to business. So don't be loosley in use of drawn graphics. Icons are welcome ofcourse

```html
<!DOCTYPE html>
<html lang="en">
<head>
<meta charset="utf-8">
<title>Client Dashboard</title>
<link href="https://fonts.googleapis.com/css2?family=Open+Sans:wght@400;600&family=Raleway:wght@400;600;700&display=swap" rel="stylesheet">
<style>
  :root{
    --page-bg:#ebebeb;
    --panel:#ffffff;
    --header-bg:#f7f7f7;
    --ink:#555555;
    --ink-soft:#9a9a9a;
    --line:#cfcfcf;
    --accent:#a6d82a;
    --compliance:#29abe2;
    --risk-issues:#2de3cf;
    --risk-alerts:#2ee585;
    --industry:#79e52b;
    --business:#b2e52c;
  }
  *{box-sizing:border-box;margin:0;padding:0}
  html,body{width:1200px;height:876px;overflow:hidden}
  body{background:var(--page-bg);font-family:"Open Sans",Arial,sans-serif;color:var(--ink);position:relative}
  .dashboard{position:absolute;left:99px;top:72px;width:1002px;height:732px;background:var(--panel);border-radius:12px;overflow:hidden}
  .topbar{position:absolute;left:0;top:0;width:100%;height:88px;background:var(--header-bg)}
  .search{position:absolute;left:90px;top:27px;width:231px;height:35px;border:1px solid #dcdcdc;background:#fff;display:flex;align-items:center;padding:0 10px}
  .search span{flex:1;font-size:12px;color:#b5b5b5}
  .user{position:absolute;right:90px;top:28px;display:flex;align-items:center;gap:14px}
  .user-name{font-family:"Open Sans",Arial,sans-serif;font-size:16px;color:#a9a9a9}
  .messages{position:relative;width:44px;height:34px}
  .messages .badge{position:absolute;left:-2px;top:-2px;width:14px;height:14px;border-radius:50%;background:var(--accent);color:#fff;font-size:9px;line-height:14px;text-align:center;font-weight:600}
  .company{position:absolute;left:90px;top:130px;width:145px;text-align:center}
  .company-mark{display:block;margin:0 auto}
  .company-name{font-family:"Raleway",Arial,sans-serif;font-weight:700;font-size:17px;color:#555;margin-top:6px;letter-spacing:.2px}
  .divider{position:absolute;left:262px;top:141px;width:1px;height:132px;background:var(--line)}
  .intro{position:absolute;left:288px;top:144px;width:622px}
  .intro p{font-size:11.6px;line-height:18px;color:#555}
  .read-more{display:flex;align-items:center;gap:7px;margin-top:10px;font-family:"Raleway",Arial,sans-serif;font-size:12px;font-weight:600;color:var(--accent)}
  .read-more i{width:17px;height:17px;border-radius:50%;background:var(--accent);color:#fff;font-style:normal;font-size:14px;line-height:17px;text-align:center}
  .alerts{position:absolute;left:0;top:0}
  .alert-label{font-family:"Raleway",Arial,sans-serif;font-size:16px;fill:#fff;letter-spacing:.3px}
</style>
</head>
<body>
<main class="dashboard">
  <header class="topbar">
    <div class="search">
      <span>Search...</span>
      <svg width="18" height="18" viewBox="0 0 18 18"><circle cx="7.5" cy="7.5" r="5.5" fill="none" stroke="#a6d82a" stroke-width="1.8"/><line x1="11.5" y1="11.5" x2="16" y2="16" stroke="#a6d82a" stroke-width="1.8" stroke-linecap="round"/></svg>
    </div>
    <div class="user">
      <span class="user-name">Hi, Mr. John Doe</span>
      <div class="messages">
        <svg width="44" height="34" viewBox="0 0 44 34"><path d="M8 6h22a6 6 0 0 1 6 6v6a6 6 0 0 1-6 6H18l-6 5v-5H8a6 6 0 0 1-6-6v-6a6 6 0 0 1 6-6z" fill="none" stroke="#d0d0d0" stroke-width="1.4"/><path d="M20 10h16a6 6 0 0 1 6 6v5a6 6 0 0 1-6 6h-2v4l-5-4h-9" fill="none" stroke="#d0d0d0" stroke-width="1.4"/></svg>
        <span class="badge">1</span>
      </div>
    </div>
  </header>

  <section class="company">
    <svg class="company-mark" width="110" height="110" viewBox="0 0 110 110"><rect x="24" y="24" width="62" height="62" fill="var(--accent)" transform="rotate(45 55 55)"/></svg>
    <div class="company-name">COMPANY NAME</div>
  </section>
  <div class="divider"></div>
  <section class="intro">
    <p>Lorem Ipsum is simply dummy text of the printing and typesetting industry. Lorem Ipsum has been the industry's standard dummy text ever since the 1500s, when an unknown printer took a galley of type and scrambled it to make a type specimen book. It has survived not only five centuries, but also the leap into electronic typesetting, remaining essentially unchanged. It was popularised in the 1960s with the release of Letraset sheets containing Lorem Ipsum passages, and more recently with desktop.</p>
    <div class="read-more"><i>+</i>READ MORE</div>
  </section>

  <svg class="alerts" width="1002" height="732" viewBox="0 0 1002 732">
    <g stroke="#fff" stroke-width="4">
      <polygon points="209,327 329,447 209,567 89,447" fill="var(--compliance)"/>
      <polygon points="500,327 620,447 500,567 380,447" fill="var(--risk-alerts)"/>
      <polygon points="792,327 912,447 792,567 672,447" fill="var(--business)"/>
      <polygon points="354,427 474,547 354,667 234,547" fill="var(--risk-issues)"/>
      <polygon points="646,427 766,547 646,667 526,547" fill="var(--industry)"/>
    </g>

    <!-- compliance issues -->
    <g fill="none" stroke="#fff" stroke-width="2">
      <rect x="186" y="380" width="34" height="44" rx="1"/>
      <line x1="192" y1="406" x2="212" y2="406"/><line x1="192" y1="413" x2="206" y2="413"/>
      <path d="M196 400l16-16 4 4-16 16h-4z"/>
    </g>
    <circle cx="224" cy="420" r="10" fill="#fff"/><path d="M219 420l4 4 6-7" fill="none" stroke="var(--compliance)" stroke-width="2"/>
    <text class="alert-label" x="209" y="472" text-anchor="middle">COMPLIANCE ISSUES</text>
    <line x1="164" y1="485" x2="254" y2="485" stroke="#fff" stroke-opacity=".7"/>
    <circle cx="209" cy="513" r="13" fill="#fff"/><text x="209" y="518" text-anchor="middle" font-size="15" font-weight="600" fill="var(--compliance)">+</text>

    <!-- risk alerts -->
    <g fill="none" stroke="#fff" stroke-width="2">
      <rect x="477" y="380" width="34" height="44" rx="1"/>
      <line x1="483" y1="406" x2="503" y2="406"/><line x1="483" y1="413" x2="497" y2="413"/>
      <path d="M487 400l16-16 4 4-16 16h-4z"/>
    </g>
    <circle cx="515" cy="420" r="10" fill="#fff"/><path d="M510 420l4 4 6-7" fill="none" stroke="var(--risk-alerts)" stroke-width="2"/>
    <text class="alert-label" x="500" y="472" text-anchor="middle">RISK ALERTS</text>
    <line x1="455" y1="485" x2="545" y2="485" stroke="#fff" stroke-opacity=".7"/>
    <circle cx="500" cy="513" r="13" fill="#fff"/><text x="500" y="518" text-anchor="middle" font-size="15" font-weight="600" fill="var(--risk-alerts)">+</text>

    <!-- business alerts -->
    <g fill="none" stroke="#fff" stroke-width="2">
      <circle cx="779" cy="394" r="9"/><circle cx="806" cy="394" r="9"/>
      <path d="M763 430v-8a10 10 0 0 1 10-10h12a10 10 0 0 1 10 10v8"/>
      <path d="M792 412h20a10 10 0 0 1 10 10v8h-22"/>
    </g>
    <circle cx="769" cy="433" r="9" fill="#fff"/><text x="769" y="438" text-anchor="middle" font-size="12" font-weight="700" fill="var(--business)">!</text>
    <text class="alert-label" x="792" y="472" text-anchor="middle">BUSSINESS ALERTS</text>
    <line x1="747" y1="485" x2="837" y2="485" stroke="#fff" stroke-opacity=".7"/>
    <circle cx="792" cy="513" r="13" fill="#fff"/><text x="792" y="518" text-anchor="middle" font-size="15" font-weight="600" fill="var(--business)">+</text>

    <!-- risk issues -->
    <path d="M354 476l30 52h-60z" fill="none" stroke="#fff" stroke-width="2.5" stroke-linejoin="round"/>
    <line x1="354" y1="494" x2="354" y2="513" stroke="#fff" stroke-width="3"/>
    <circle cx="354" cy="520" r="2" fill="#fff"/>
    <text class="alert-label" x="354" y="572" text-anchor="middle">RISK ISSUES</text>
    <line x1="309" y1="585" x2="399" y2="585" stroke="#fff" stroke-opacity=".7"/>
    <circle cx="354" cy="613" r="13" fill="#fff"/><text x="354" y="618" text-anchor="middle" font-size="15" font-weight="600" fill="var(--risk-issues)">+</text>

    <!-- industry alerts -->
    <g fill="none" stroke="#fff" stroke-width="2">
      <path d="M618 528v-32h8v14l10-8v8l10-8v8l10-8v26z"/>
      <path d="M620 490c-3-4 3-6 0-10M630 490c-3-4 3-6 0-10"/>
    </g>
    <circle cx="668" cy="524" r="9" fill="#fff"/><text x="668" y="529" text-anchor="middle" font-size="12" font-weight="700" fill="var(--industry)">!</text>
    <text class="alert-label" x="646" y="572" text-anchor="middle">INDUSTRY ALERTS</text>
    <line x1="601" y1="585" x2="691" y2="585" stroke="#fff" stroke-opacity=".7"/>
    <circle cx="646" cy="613" r="13" fill="#fff"/><text x="646" y="618" text-anchor="middle" font-size="15" font-weight="600" fill="var(--industry)">+</text>
  </svg>
</main>
</body>
</html>
```